Lawn Company needs design work on a service call flyer!

We are a lawn care company that fertilizes and sprays lawns. This design is meant to be left behind at the customers house after a lawn application has been done too let them know what we have done.

The finished design will be printed on A6 paper (4.1 x 5.8 inches)

I have attached PDF files of the text that I want on the front of the document and the back of the document. I also included a sample design that I had been working on to give some idea what I would like. I don't want the same design, but you can use it as a building block for something new or come up with something entirely different.

FRONT: The front of the design is most important.

BACK: Other then the text the design should be minimal. If possible I would like an outline of the trees in my logo to be a backdrop. I have attached a PDF of the back of my business card as an example

The winning design will be a professional looking document that flows and reflects a lawn care business. Please contact me if you have any questions. I will only pick a design that is better then my current template.

Thank You

Target Market(s)

Lawn Care Customers

Industry/Entity Type

Lawn Care

Requirements
Must have
• 1. Our Logo
• 2. The attached text for the front & back of document
• 3. Our phone number (604-918-4471)
• 4. Our Email address (fenwickturfcare@mailora.net)
Nice to have
• A green theme with flowing graphics
Should not have
• any pictures of houses, people, or tools
• Don't copy the text or design from my design template. It is outdated, is it meant to be an example only

```html
<!DOCTYPE html>
<html lang="en">
<head>
<meta charset="utf-8">
<title>Fenwick Turf Care – Service Call Card</title>
<link href="https://fonts.googleapis.com/css2?family=Open+Sans:ital,wght@0,700;0,800;1,700&family=Arimo:ital,wght@0,400;0,700;1,400;1,700&display=swap" rel="stylesheet">
<style>
  :root {
    --stage: #e4e6e8;
    --sky-top: #b9d9f3;
    --sky-bottom: #ffffff;
    --ink: #1e1e1e;
    --ink-soft: #333;
    --brand-green: #3f9a2e;
    --leaf-green: #7cc142;
    --grass-dark: #3d7d1c;
    --grass-light: #9fd35a;
    --band-grey: #4a4a4a;
    --tree-ghost: rgba(120, 140, 155, 0.28);
  }
  * { box-sizing: border-box; margin: 0; padding: 0; }
  html, body { width: 1200px; height: 900px; overflow: hidden; }
  body {
    background: var(--stage);
    font-family: "Arimo", Arial, sans-serif;
    color: var(--ink);
    position: relative;
  }
  .card {
    position: absolute;
    width: 680px;
    height: 420px;
    overflow: hidden;
    box-shadow: 0 6px 18px rgba(0,0,0,0.25);
  }

  /* ---------- Front ---------- */
  .card--front {
    left: 60px; top: 24px;
    background: linear-gradient(180deg, var(--sky-top) 0%, #dcecf9 40%, var(--sky-bottom) 78%);
  }
  .brand {
    position: absolute; right: 22px; top: 18px;
    display: flex; align-items: center; gap: 6px;
    font-family: "Open Sans", Arial, sans-serif;
    font-weight: 800; font-size: 15px; color: var(--brand-green);
    letter-spacing: 0.5px;
  }
  .brand__mark { width: 12px; height: 12px; background: var(--brand-green); }
  .front__body { position: absolute; left: 28px; top: 62px; right: 28px; }
  .field-title {
    font-family: "Open Sans", Arial, sans-serif;
    font-weight: 800; font-size: 13px; text-transform: uppercase;
    margin-bottom: 18px; white-space: nowrap;
  }
  .blank { display: inline-block; border-bottom: 1px solid var(--ink); vertical-align: bottom; }
  .intro { font-size: 10px; margin: 4px 0 10px; }
  .checklist { list-style: none; font-size: 10px; }
  .checklist li { display: flex; align-items: center; gap: 10px; margin-bottom: 10px; }
  .checkbox { width: 10px; height: 10px; border: 1.5px solid var(--ink); }
  .watering { font-size: 10px; margin-top: 14px; }
  .pledge { font-size: 9.5px; font-style: italic; margin-top: 16px; line-height: 1.35; }
  .grass {
    position: absolute; left: 0; right: 0; bottom: 0; height: 96px;
    background: linear-gradient(180deg, rgba(159,211,90,0) 0%, var(--grass-light) 30%, var(--grass-dark) 100%);
  }

  /* ---------- Back ---------- */
  .card--back {
    left: 460px; top: 464px;
    background: linear-gradient(180deg, #c6e0f5 0%, #e4f0fa 100%);
  }
  .tree-backdrop {
    position: absolute; left: 30px; right: 30px; top: 150px; bottom: 20px;
    background: radial-gradient(ellipse at 50% 60%, var(--tree-ghost), rgba(120,140,155,0) 70%);
  }
  .guide-band {
    position: absolute; left: 34px; right: 34px; top: 16px; height: 20px;
    background: var(--band-grey);
    color: var(--leaf-green);
    font-family: "Open Sans", Arial, sans-serif; font-weight: 800; font-size: 11.5px;
    display: flex; align-items: center; justify-content: center; letter-spacing: 0.3px;
  }
  .guides { position: absolute; left: 30px; right: 30px; top: 44px; font-size: 9.4px; line-height: 1.28; color: var(--ink-soft); }
  .guides h3 { font-size: 9.5px; font-weight: 700; font-style: italic; text-decoration: underline; color: var(--ink); margin: 6px 0 1px; }
  .guides ul { margin-left: 22px; }
  .contact {
    position: absolute; left: 50%; transform: translateX(-50%); bottom: 34px;
    background: var(--band-grey); color: #fff; padding: 5px 12px;
  }
  .contact__row { display: flex; align-items: center; gap: 6px; }
  .contact__phone { font-family: "Open Sans", Arial, sans-serif; font-weight: 700; font-size: 15px; color: var(--leaf-green); }
  .contact__mail { font-size: 8.5px; }
  .stripe { position: absolute; left: 0; right: 0; bottom: 0; height: 14px; background: var(--leaf-green); }
</style>
</head>
<body>

<section class="card card--front">
  <div class="brand"><span class="brand__mark"></span>FENWICK TURF CARE</div>
  <div class="front__body">
    <p class="field-title">Application Time / Date: <span class="blank" style="width:70px"></span></p>
    <p class="field-title">Your lawn has been professionally serviced today by <span class="blank" style="width:100px"></span></p>
    <p class="intro">Today's application consists of</p>
    <ul class="checklist">
      <li><span class="checkbox"></span>Seasonally Balanced Slow Release Fertilizer</li>
      <li><span class="checkbox"></span>Broadleaf Weed Control (Please keep off the lawn until it is thoroughly dry)</li>
      <li><span class="checkbox"></span>Other <span class="blank" style="width:110px"></span></li>
    </ul>
    <p class="watering">Please begin watering the lawn &nbsp;<span class="blank" style="width:110px"></span> after application</p>
    <p class="pledge">"We strive to complete work in a professional manner each and every visit. If you are not satisfied with the level of service you are receiving please contact us.<br>We value your business and wish to maintain long-term relationships with our customers."</p>
  </div>
  <div class="grass" role="img" aria-label="Strip of green grass blades along the bottom edge"></div>
</section>

<section class="card card--back">
  <div class="tree-backdrop" role="img" aria-label="Faint outline of trees as a backdrop"></div>
  <div class="guide-band">FOR BEST RESULTS PLEASE FOLLOW THESE GENERAL GUIDELINES</div>
  <div class="guides">
    <h3>WATERING YOUR LAWN</h3>
    <p>When rainfall is not sufficient to meet your lawns watering needs, follow these guidelines for a lush green lawn</p>
    <ul>
      <li>Your lawn requires approx. 1 - 1.5 inches of water per week, sometimes more in hot, dry weather</li>
      <li>Avoid short frequent watering. It is best to water deeply once every 5 - 7 days. This encourages deep root growth.</li>
      <li>You can use a Frisbee or an empty tuna can to measure the amount you have watered. Just place it in the path of the sprinkler and when it is full, move your sprinkler to a new location.</li>
      <li>Aerating your lawn once a year will help your lawn utilize more water and prevent unnecessary runoff</li>
    </ul>
    <h3>MOWING YOUR LAWN</h3>
    <p>Mowing your lawn properly can make all the difference in how it looks throughout the year</p>
    <ul>
      <li>You should mow your lawn at 2.5 - 3 inches (no shorter). Mowing at this length helps shade your roots and provides more leaf surface for your lawn to manufacture its own food. As an added bonus it will help your lawn retain its moisture and reduce watering requirements.</li>
      <li>As a general rule, try not to remove more than 1/3 of the leaf blade in a single mowing. During periods of heavy growth, this may mean mowing more frequently than usual.</li>
      <li>Always ensure your lawn mower is maintained and the blade is sharp so that it cuts cleanly.</li>
      <li>Your last mowing in the fall should be shorter, about 2 inches</li>
    </ul>
  </div>
  <div class="contact">
    <div class="contact__row">
      <svg width="12" height="12" viewBox="0 0 24 24" aria-hidden="true"><path fill="#7cc142" d="M6.6 10.8a15.1 15.1 0 0 0 6.6 6.6l2.2-2.2c.3-.3.7-.4 1-.2 1.1.4 2.3.6 3.6.6.6 0 1 .4 1 1V20c0 .6-.4 1-1 1A17 17 0 0 1 3 4c0-.6.4-1 1-1h3.5c.6 0 1 .4 1 1 0 1.3.2 2.5.6 3.6.1.3 0 .7-.2 1z"/></svg>
      <span class="contact__phone">604 918 44 71</span>
    </div>
    <div class="contact__row">
      <svg width="10" height="8" viewBox="0 0 20 14" aria-hidden="true"><rect x="0.5" y="0.5" width="19" height="13" fill="none" stroke="#fff"/><path d="M0.5 0.5 10 8l9.5-7.5" fill="none" stroke="#fff"/></svg>
      <span class="contact__mail">fenwickturfcare@mailora.net</span>
    </div>
  </div>
  <div class="stripe"></div>
</section>

</body>
</html>
```